MossVane Spa, Skincare and Cosmetics website

I need a website for MossVane (putting the glow back into people's skin) which allows viewers to access information about Beauty Spa packaging and facilities as well as online skincare and cosmetic products. Our distinctive difference is that our products are certified organic. We want to target a luxury high income niche market (age 30-50). I want all colours to be "baby colours" preferably background to be "baby metallic pink" (but please don't make the website too immature) with curves as patterns. I want a romantic vintage look.

The website needs to look:
1. elegant (prestige and luxury)
2. bright (baby colours mainly)
3. European curves and signature patterns
4. Can include Pearl related pics (but not a must)

The website pages needs to have:
1. pages ordering skincare/cosmetics
2. shopping cart and payment
3. about us and about our product differences
4. contact us
5. booking for spa treatments and packages

I have attached our logo and also packaging label styles.

Industry/Entity Type

Cosmetics

```html
<!DOCTYPE html>
<html lang="en">
<head>
<meta charset="utf-8">
<title>MossVane Spa, Skincare and Cosmetics</title>
<link rel="stylesheet" href="https://fonts.googleapis.com/css2?family=EB+Garamond:wght@400;500&family=Open+Sans:wght@400;600;700&family=Roboto+Condensed:wght@400&display=swap">
<style>
:root{
  --page:#f7f5f5;
  --band:#efebea;
  --white:#ffffff;
  --rose:#b4968a;
  --rose-soft:#cfb2a7;
  --rose-line:#dcc8c0;
  --text:#6b6b6b;
  --text-dark:#444444;
  --grey-btn:#8c8c8c;
  --line:#dddddd;
  --footer:#f1f1f1;
}
*{box-sizing:border-box;margin:0;padding:0}
html,body{width:828px;height:1200px;overflow:hidden;background:var(--page)}
body{font-family:"Open Sans",Arial,sans-serif;color:var(--text);position:relative}
.abs{position:absolute}
.top-band{left:0;top:0;width:828px;height:343px;background:var(--band)}

/* header */
.site-header{left:92px;top:0;width:657px;height:144px;background:var(--white);border-radius:0 0 10px 10px;box-shadow:0 1px 3px rgba(0,0,0,.08)}
.site-header::after{content:"";position:absolute;left:4px;right:4px;bottom:4px;border-bottom:1px dashed var(--rose-line)}
.brand{left:38px;top:46px;display:flex;align-items:center;gap:8px}
.brand-dot{width:22px;height:22px;border-radius:50%;background:var(--rose-soft)}
.brand-name{font-family:"EB Garamond",Georgia,serif;font-size:27px;color:var(--rose);letter-spacing:1px}
.cart-divider{left:455px;top:30px;width:1px;height:58px;background:#e6e6e6}
.cart-icon{left:470px;top:38px;width:40px;height:40px;border-radius:50%;border:1px solid #ddd;display:flex;align-items:center;justify-content:center}
.cart-label{left:518px;top:42px;font-family:"Roboto Condensed",Arial,sans-serif;font-size:11px;color:#555}
.cart-label small{font-size:9.5px;color:#777}
.cart-total{left:518px;top:58px;font-size:15px;color:#555}
.checkout-btn{left:560px;top:60px;width:56px;height:17px;background:var(--grey-btn);color:#fff;font-size:10.5px;text-align:center;line-height:17px;border:1px solid #777}
.main-nav{left:0;top:115px;width:657px;display:flex;justify-content:center;gap:0}
.main-nav a{font-family:"Roboto Condensed",Arial,sans-serif;font-size:13.5px;color:#555;text-decoration:none;padding:0 11px;height:29px;line-height:29px;margin:0 4px}
.main-nav a.is-active{background:var(--rose-soft);color:#fff}

/* hero */
.hero{left:92px;top:161px;width:657px;height:256px;background:var(--white);border-radius:6px;box-shadow:0 1px 4px rgba(0,0,0,.1);overflow:hidden}
.hero-photo{left:0;top:0;width:328px;height:256px;background:linear-gradient(120deg,#f3f1ef,#e9dcd3 55%,#d9c2b6)}
.hero-dots{left:182px;top:237px;display:flex;gap:4px}
.hero-dots span{width:7px;height:7px;border-radius:50%;background:#fff;box-shadow:0 0 1px rgba(0,0,0,.3)}
.hero-dots span.on{background:#555}
.hero-title{left:352px;top:60px;font-family:"EB Garamond",Georgia,serif;font-size:25px;color:var(--rose);letter-spacing:.5px}
.hero-sub{left:352px;top:96px;font-family:"EB Garamond",Georgia,serif;font-size:11.5px;line-height:15px;color:var(--rose);text-transform:uppercase;letter-spacing:.3px}
.shop-btn{left:353px;top:139px;width:107px;height:28px;background:var(--rose-soft);color:#fff;font-weight:700;font-size:12.5px;display:flex;align-items:center;justify-content:center;gap:6px;border:1px solid #bfa095}
.hero-jar{left:479px;top:340px;width:142px;height:108px;border-radius:50% 50% 18px 18px;background:linear-gradient(180deg,#f7f5f0,#dedbd3)}

/* about */
.section-title{font-family:"EB Garamond",Georgia,serif;font-size:19px;color:var(--rose);letter-spacing:.4px;text-transform:uppercase}
.about-title{left:94px;top:480px}
.about-text{left:95px;top:515px;width:300px;font-size:10.6px;line-height:16.2px;color:var(--text)}
.about-text p+p{margin-top:16px}
.services{left:417px;top:496px;width:331px;height:154px;background:var(--white);border:1px solid #e2e2e2}
.services-photo{left:0;top:0;width:138px;height:152px;background:linear-gradient(135deg,#c8a58f,#e8cfc0 50%,#b38a72)}
.services-title{left:156px;top:18px;font-size:18px}
.services-list{left:160px;top:53px;list-style:none;font-size:10.6px;color:#555}
.services-list li{height:18px;display:flex;align-items:center;gap:8px}

/* products */
.products-title{left:94px;top:692px}
.view-all{left:632px;top:693px;width:115px;height:22px;border:1px solid var(--rose-soft);background:#fff;font-size:10px;color:#555;display:flex;align-items:center;justify-content:center;gap:8px;border-radius:2px}
.product-card{top:734px;width:144px;height:191px;background:#fff;border:1px solid #ddd;box-shadow:0 1px 3px rgba(0,0,0,.1);text-align:center}
.product-image{left:32px;top:16px;width:80px;height:78px}
.product-name{position:absolute;left:0;right:0;top:104px;font-size:13px;font-weight:600;color:#444}
.product-desc{position:absolute;left:10px;right:10px;top:124px;font-size:8.7px;line-height:11px;color:#666}
.product-divider{left:12px;right:12px;top:150px;height:0}
.product-price{left:12px;top:158px;font-size:15px;font-weight:700;color:#555}
.price-sep{left:65px;top:154px;width:1px;height:28px;background:#e5e5e5}
.buy-btn{left:72px;top:158px;width:67px;height:21px;background:var(--grey-btn);color:#fff;font-size:11px;line-height:21px;border:1px solid #777}

/* footer */
.footer{left:0;top:970px;width:828px;height:153px;background:var(--footer)}
.footer-col{top:994px}
.footer-col h4{font-size:10.8px;font-weight:600;color:#444;margin-bottom:9px}
.footer-col ul{list-style:none;font-size:8.8px;color:#555;line-height:16px;padding-left:2px}
.news-input{left:558px;top:1019px;width:124px;height:21px;background:#fff;border:1px solid #ddd;font-size:8.5px;color:#aaa;padding-left:10px;line-height:19px}
.news-btn{left:689px;top:1019px;width:56px;height:21px;background:var(--rose-soft);color:#fff;font-weight:700;font-size:11px;text-align:center;line-height:21px}
.social{top:1059px;width:30px;height:30px;border-radius:50%;border:1px solid #bbb}
.copyright{left:0;top:1144px;width:828px;text-align:center;font-size:11px;color:#666}
.legal{left:0;top:1164px;width:828px;text-align:center;font-size:8.5px;color:#444}
</style>
</head>
<body>
<div class="abs top-band"></div>

<header class="abs site-header">
  <div class="abs brand"><span class="brand-dot"></span><span class="brand-name">MossVane</span></div>
  <div class="abs cart-divider"></div>
  <div class="abs cart-icon">
    <svg width="18" height="20" viewBox="0 0 18 20"><rect x="2" y="6" width="14" height="13" fill="var(--rose-line)"/><path d="M6 7V4a3 3 0 0 1 6 0v3" fill="none" stroke="var(--rose-line)" stroke-width="1.5"/></svg>
  </div>
  <div class="abs cart-label">YOUR CART <small>(2 items)</small></div>
  <div class="abs cart-total">$300</div>
  <div class="abs checkout-btn">Checkout</div>
  <nav class="abs main-nav">
    <a>HOME</a><a class="is-active">ABOUT</a><a>SPA</a><a>CAFE</a><a>SHOP</a><a>GALLERY</a><a>EVENTS</a><a>CONTACT US</a>
  </nav>
</header>

<section class="abs hero">
  <div class="abs hero-photo" role="img" aria-label="Spa guest relaxing with a face mask and towel"></div>
  <div class="abs hero-dots"><span></span><span class="on"></span><span></span><span></span></div>
  <h1 class="abs hero-title">YOUR HEADING HERE</h1>
  <p class="abs hero-sub">This is Layerset's version &nbsp;of<br>lorem ipsum.</p>
  <div class="abs shop-btn">
    <svg width="12" height="11" viewBox="0 0 12 11"><path d="M0 1h2l2 6h6l2-5H3" fill="none" stroke="#fff" stroke-width="1.4"/><circle cx="5" cy="9.5" r="1.1" fill="#fff"/><circle cx="9" cy="9.5" r="1.1" fill="#fff"/></svg>
    SHOP NOW
  </div>
</section>
<div class="abs hero-jar" role="img" aria-label="Open jar of MossVane face cream"></div>

<h2 class="abs section-title about-title">MossVane Beauty Spa</h2>
<div class="abs about-text">
  <p>This is Layerset's version &nbsp;of Lorem Ipsum. Proin gravida nibh vel velit auctor aliquet. Aenean sollicitudin, lorem quis bibendum auctor, nisi elit consequat ipsum, nec sagittis sem nibh id elit. Duis sed odio sit amet nibh vulputate cursus a sit amet mauris. Morbi accumsan ipsum velit.</p>
  <p>Nam nec tellus a odio tincidunt auctor a ornare odio. Sed non mauris vitae erat consequat</p>
</div>

<section class="abs services">
  <div class="abs services-photo" role="img" aria-label="Cream being applied to the skin"></div>
  <h3 class="abs section-title services-title">Our Services</h3>
  <ul class="abs services-list">
    <li><svg width="5" height="8" viewBox="0 0 5 8"><path d="M1 1l3 3-3 3" fill="none" stroke="#777"/></svg>This is Layerset's version</li>
    <li><svg width="5" height="8" viewBox="0 0 5 8"><path d="M1 1l3 3-3 3" fill="none" stroke="#777"/></svg>Lorem Ipsum.</li>
    <li><svg width="5" height="8" viewBox="0 0 5 8"><path d="M1 1l3 3-3 3" fill="none" stroke="#777"/></svg>Proin gravida nibh</li>
    <li><svg width="5" height="8" viewBox="0 0 5 8"><path d="M1 1l3 3-3 3" fill="none" stroke="#777"/></svg>Vel velit auctor aliquet.</li>
    <li><svg width="5" height="8" viewBox="0 0 5 8"><path d="M1 1l3 3-3 3" fill="none" stroke="#777"/></svg>Aenean sollicitudin</li>
  </ul>
</section>

<h2 class="abs section-title products-title">Popular Products</h2>
<div class="abs view-all">View all Products <svg width="7" height="8" viewBox="0 0 7 8"><path d="M1 1l3 3-3 3M3.5 1l3 3-3 3" fill="none" stroke="#555"/></svg></div>

<article class="abs product-card" style="left:92px">
  <div class="abs product-image" role="img" aria-label="Gold-lidded cream jar" style="background:linear-gradient(180deg,#d9b94a 0 35%,#f2f0ec 35%,#dcdad5)"></div>
  <div class="product-name">Nordic Bloom</div>
  <div class="product-desc">Verde Herbals Pedicure Manicure &nbsp;(135 ml)</div>
  <div class="abs product-price">$210</div><div class="abs price-sep"></div>
  <div class="abs buy-btn">Buy now</div>
</article>
<article class="abs product-card" style="left:265px">
  <div class="abs product-image" role="img" aria-label="Two cream tubes" style="background:linear-gradient(90deg,#f6f6f8,#c9c8d4 50%,#e2e5d6)"></div>
  <div class="product-name">Calmwater</div>
  <div class="product-desc">Calmwater Spa Cream &amp; red Body Butter &nbsp;(135 ml)</div>
  <div class="abs product-price">$35.8</div><div class="abs price-sep"></div>
  <div class="abs buy-btn">Buy now</div>
</article>
<article class="abs product-card" style="left:435px">
  <div class="abs product-image" role="img" aria-label="Boxed body lotion with tube" style="background:linear-gradient(90deg,#fff 15%,#7a3d40 15%,#5e2d30 85%,#fff 85%)"></div>
  <div class="product-name">Tide of Calm</div>
  <div class="product-desc">Verde Herbals Pedicure Manicure &nbsp;(135 ml)</div>
  <div class="abs product-price">$580</div><div class="abs price-sep"></div>
  <div class="abs buy-btn">Buy now</div>
</article>
<article class="abs product-card" style="left:604px">
  <div class="abs product-image" role="img" aria-label="White and burgundy product box" style="background:linear-gradient(90deg,#f3f0ee 50%,#8a2e33 50%)"></div>
  <div class="product-name">RL Spa</div>
  <div class="product-desc">Verde Herbals Pedicure Manicure &nbsp;(135 ml)</div>
  <div class="abs product-price">$110</div><div class="abs price-sep"></div>
  <div class="abs buy-btn">Buy now</div>
</article>

<footer class="abs footer"></footer>
<div class="abs footer-col" style="left:89px"><h4>Company info</h4><ul><li>About Us</li><li>The Lilac e-Magazine</li><li>Customer Service</li><li>FAQ</li><li>Contact Us</li></ul></div>
<div class="abs footer-col" style="left:221px"><h4>Store</h4><ul><li>Men</li><li>Skin Care</li><li>Make Up</li><li>Hair Care</li><li>Body Care</li></ul></div>
<div class="abs footer-col" style="left:307px"><h4>Customer service</h4><ul><li>Feedback</li><li>Cancellation &amp; Returns</li><li>Terms &amp; Conditions</li><li>Payment Methods</li></ul></div>
<div class="abs footer-col" style="left:433px"><h4>Customer service</h4><ul><li>Feedback</li><li>Cancellation &amp; Returns</li><li>Terms &amp; Conditions</li><li>Payment Methods</li></ul></div>
<div class="abs footer-col" style="left:558px"><h4>Subscribe for Newsletter</h4></div>
<div class="abs news-input">email address</div>
<div class="abs news-btn">Submit</div>
<div class="abs social" style="left:561px"></div>
<div class="abs social" style="left:602px"></div>
<div class="abs social" style="left:644px"></div>

<div class="abs copyright">Copyright © 2014 MossVane. All Rights Reserved.</div>
<div class="abs legal">Disclaimer &nbsp;|&nbsp; Privacy policy &nbsp;|&nbsp; Sitemap xml &nbsp;|&nbsp; html</div>
</body>
</html>
```